Vel-Trax.ch is looking for business card letterhead and envelope C5 with WOW effect

We need a strong business card for our company Vel-Trax.ch, logo is available. You want a black or dark background on which the logo Stark r% 26 # 252; appears. Letterhead and envelope in C5 format should be in a similar design, but does not have to be We need a strong business card for our company Vel-Trax.ch, logo is available. A black or dark background is desired, on which the logo Stark comes across. The letterhead and the envelope in C5 format should have a similar design.

Target Market(s)

Private customers as well as entrepreneurs

Contact Information for Business Card

E-mail: info@vel-trax.ch
Web.www.Vel-Trax.ch
Tel: +41 ( 0 ) 79 684 3027
Adresse:
Lindenhaldeweg 14
9403 Brenzikon

Hier kann man Icons verwenden für Email,Tel und Adressse

Font styles to use
Other font styles liked:
• Dubai,bold

Colors

Designer to choose colors to be used in the design.

Requirements
Must have
• WOW effect
Nice to have
• R% 26 # 252; back business card with our service listings. - VEHICLE LABELING - SHOP WINDOW LABELING - STICKERS AND MUCH MORE ... in red color

```html
<!DOCTYPE html>
<html lang="en">
<head>
<meta charset="utf-8">
<title>Vel-Trax.ch Business Card</title>
<link href="https://fonts.googleapis.com/css2?family=Mulish:wght@400;600;800&display=swap" rel="stylesheet">
<style>
  :root {
    --backdrop: #d6d6d4;
    --card-dark: #232323;
    --card-light: #ffffff;
    --brand-yellow: #f9c516;
    --text-grey: #555555;
    --font-main: "Mulish", Arial, sans-serif;
  }
  * { box-sizing: border-box; margin: 0; padding: 0; }
  html, body {
    width: 1200px; height: 913px; overflow: hidden;
    background: var(--backdrop);
    font-family: var(--font-main);
  }
  .card {
    position: absolute;
    width: 600px; height: 353px;
    border-radius: 4px;
    box-shadow: 0 6px 18px rgba(0,0,0,0.18);
  }
  /* Back side */
  .card-back { left: 80px; top: 70px; background: var(--card-dark); }
  .brand-name {
    position: absolute; left: 56px; top: 110px;
    display: flex; align-items: center; gap: 18px;
    color: var(--brand-yellow);
    font-weight: 800; font-size: 62px; letter-spacing: 2px;
    white-space: nowrap;
  }
  .brand-mark {
    width: 34px; height: 34px; background: var(--brand-yellow);
  }
  .service-list {
    position: absolute; right: 40px; top: 212px;
    list-style: none; text-align: right;
    color: var(--brand-yellow);
    font-weight: 800; font-size: 15px; letter-spacing: 0.5px; line-height: 24px;
  }
  .service-list li::after {
    content: ""; display: inline-block;
    width: 9px; height: 9px; border-radius: 50%;
    background: var(--brand-yellow);
    margin-left: 12px; vertical-align: 1px;
  }
  /* Front side */
  .card-front { left: 520px; top: 480px; background: var(--card-light); }
  .person { position: absolute; right: 36px; top: 36px; text-align: right; }
  .person-name {
    color: var(--brand-yellow); font-weight: 800; font-size: 24px; letter-spacing: 1px;
  }
  .person-role {
    color: var(--text-grey); font-weight: 400; font-size: 15px; letter-spacing: 1px; margin-top: 2px;
  }
  .address {
    position: absolute; right: 36px; top: 140px; text-align: right;
    color: var(--text-grey); font-size: 15px; line-height: 21px;
  }
  .divider {
    position: absolute; right: 36px; top: 192px;
    width: 62px; height: 2px; background: var(--brand-yellow);
  }
  .contact-list {
    position: absolute; right: 36px; top: 214px;
    list-style: none; text-align: right;
    color: var(--text-grey); font-size: 15px; line-height: 25px;
  }
  .contact-list li { display: flex; justify-content: flex-end; align-items: center; gap: 10px; }
  .contact-icon { width: 14px; height: 14px; color: var(--brand-yellow); flex: none; }
  .front-brand {
    position: absolute; left: 40px; bottom: 40px;
    color: var(--brand-yellow); font-weight: 800; font-size: 34px; letter-spacing: 1px;
    white-space: nowrap;
  }
</style>
</head>
<body>
  <section class="card card-back">
    <div class="brand-name"><span class="brand-mark"></span>VEL-TRAX.CH</div>
    <ul class="service-list">
      <li>VEHICLE LABELING</li>
      <li>SHOP WINDOW LABELING</li>
      <li>STICKERS AND MUCH MORE</li>
    </ul>
  </section>

  <section class="card card-front">
    <div class="person">
      <div class="person-name">LUKAS BRENNER</div>
      <div class="person-role">DIRECTOR</div>
    </div>
    <div class="address">Lindenhaldeweg 14<br>9418 Brenzikon</div>
    <div class="divider"></div>
    <ul class="contact-list">
      <li>+41 ( 0 ) 79 684 3027
        <svg class="contact-icon" viewBox="0 0 24 24" aria-hidden="true"><path fill="currentColor" d="M6.6 10.8a15.1 15.1 0 0 0 6.6 6.6l2.2-2.2a1 1 0 0 1 1-.25 11.4 11.4 0 0 0 3.6.57 1 1 0 0 1 1 1V20a1 1 0 0 1-1 1A17 17 0 0 1 3 4a1 1 0 0 1 1-1h3.5a1 1 0 0 1 1 1c0 1.25.2 2.45.57 3.57a1 1 0 0 1-.25 1z"/></svg>
      </li>
      <li>info@vel-trax.ch
        <svg class="contact-icon" viewBox="0 0 24 24" aria-hidden="true"><path d="M2 5h20v14H2z M2 5l10 8 10-8" fill="none" stroke="currentColor" stroke-width="2"/></svg>
      </li>
      <li>www.Vel-Trax.ch
        <svg class="contact-icon" viewBox="0 0 24 24" aria-hidden="true"><circle cx="12" cy="12" r="9" fill="none" stroke="currentColor" stroke-width="2"/><path d="M3 12h18M12 3c3 3 3 15 0 18M12 3c-3 3-3 15 0 18" fill="none" stroke="currentColor" stroke-width="1.6"/></svg>
      </li>
    </ul>
    <div class="front-brand">VEL-TRAX.CH</div>
  </section>
</body>
</html>
```